Wattlebrook Lather Co needs packaging for Bars of Soap

I need a design for packaging bars of soap. My soaps are focused on quality ingredients, utilising Australian Clay's and unique Australian essential oils. The Soaps are designed to benefit the skin by lightly exfoliating, cleansing while moisturizing and softening the skin.

I am wanting a soap box designed.
The box should be 95mm x 70mm x 28mm
Have an upmarket quality feel.
I am thinking of using grey, but am open to other natural colours.
The box will have the logo, web address, space left so I can add the ingredient list.
The text 'Handcrafted in Fernhollow' on the box. (If it fits comfortably)

Target Market(s)

25-50yrs , health and body conscious

Industry/Entity Type

Health And Wellness

Requirements
Must have
• include the web address.
• space for the scent/type of clay for each soap. This will change, as will the ingredients as I create new soaps. I would like the ability to change this as required easily myself if possible?
Nice to have
• I am swaying towards grey but am not locked in to it.
• Handcrafted in Fernhollow (text added on the box)

```html
<!DOCTYPE html>
<html lang="en">
<head>
<meta charset="UTF-8">
<title>Wattlebrook Lather Co — Soap Box Panels</title>
<link href="https://fonts.googleapis.com/css2?family=Amatic+SC:wght@400;700&family=Gochi+Hand&display=swap" rel="stylesheet">
<style>
  :root {
    --backdrop: #c5e7e5;
    --panel-grey: #c9c9c9;
    --panel-light: #e4e4e2;
    --panel-cream: #e6e8d8;
    --label-white: #f3f3f4;
    --ink: #4a4a4a;
    --ink-soft: #6b6b6b;
    --ribbon: #d8d8d8;
  }
  * { margin: 0; padding: 0; box-sizing: border-box; }
  html, body {
    width: 1200px; height: 1200px; overflow: hidden;
    background: var(--backdrop);
  }
  .stage { position: relative; width: 1200px; height: 1200px; }
  .box-panel {
    position: absolute; top: 320px;
    width: 440px; height: 560px;
  }
  .box-panel--back { left: 120px; }
  .box-panel--front { left: 640px; }
  .panel-pattern {
    position: absolute; inset: 0;
    background:
      radial-gradient(circle at 78% 18%, var(--panel-light) 0 18%, transparent 19%),
      radial-gradient(ellipse at 30% 75%, var(--panel-cream) 0 22%, transparent 23%),
      linear-gradient(160deg, var(--panel-light) 0%, var(--panel-grey) 40%, var(--panel-cream) 65%, var(--panel-grey) 100%);
  }
  .label {
    position: absolute;
    background: var(--label-white);
    display: flex; flex-direction: column; align-items: center;
  }
  .label-frame {
    position: absolute; inset: 10px;
    border: 4px solid var(--ink);
  }
  .box-panel--front .label {
    left: 173px; top: 110px; width: 212px; height: 320px;
  }
  .product-name {
    position: relative;
    margin-top: 46px;
    font-family: "Gochi Hand", cursive;
    font-size: 42px; line-height: 1; font-weight: 400;
    color: var(--ink); text-align: center;
  }
  .name-divider {
    position: relative; margin-top: 30px;
    width: 26px; height: 2px; background: var(--ink-soft);
  }
  .brand-name {
    position: relative; margin-top: 24px;
    font-family: "Amatic SC", sans-serif; font-weight: 400;
    font-size: 26px; line-height: 1; text-align: center;
    color: var(--ink);
  }
  .web-address {
    position: relative; margin-top: 22px;
    font-family: "Amatic SC", sans-serif; font-weight: 700;
    font-size: 11px; letter-spacing: 0.5px;
    color: var(--ink);
  }
  .box-panel--back .label {
    left: 177px; top: 118px; width: 211px; height: 320px;
  }
  .ingredients {
    position: relative; margin-top: 38px; padding: 0 18px;
    font-family: "Amatic SC", sans-serif; font-weight: 700;
    font-size: 11.5px; line-height: 1.4; text-align: center;
    color: var(--ink-soft); text-transform: uppercase;
  }
  .ribbon { position: absolute; left: 18px; bottom: 40px; }
  .ribbon-text {
    font-family: "Amatic SC", sans-serif; font-weight: 700;
    font-size: 10px; fill: var(--ink);
  }
</style>
</head>
<body>
<main class="stage">

  <section class="box-panel box-panel--back">
    <div class="panel-pattern" role="img" aria-label="Abstract grey and cream brush-stroke pattern with dotted shapes"></div>
    <div class="label">
      <div class="label-frame"></div>
      <p class="ingredients">
        Ingredients:<br>
        Lorem ipsum dolor sit amet,<br>
        ad omnium tibique neglegentur qui,<br>
        putent integre definiebas vis eu,<br>
        est et dicunt oblique hendrerit.<br>
        Dico eligendi deleniti ne cum,<br>
        mea modus mediocrem ne.<br>
        Ex ius voluptaria honestatis reprehendunt,<br>
        an cum alia dolor inermis.<br>
        Eos ex suas vide imperdiet,<br>
        usu no fabellas suavitate explicari.
      </p>
      <svg class="ribbon" width="175" height="30" viewBox="0 0 175 30">
        <polygon points="0,8 14,8 10,15 14,22 0,22 4,15" fill="var(--ribbon)" stroke="var(--ink)" stroke-width="1"/>
        <polygon points="175,4 160,4 164,11 160,18 175,18 171,11" fill="var(--ribbon)" stroke="var(--ink)" stroke-width="1"/>
        <rect x="10" y="5" width="155" height="18" fill="var(--ribbon)" stroke="var(--ink)" stroke-width="1" transform="rotate(-3 87 14)"/>
        <circle cx="26" cy="15" r="1.6" fill="var(--ink-soft)"/>
        <circle cx="148" cy="11" r="1.6" fill="var(--ink-soft)"/>
        <text class="ribbon-text" x="87" y="17" text-anchor="middle" transform="rotate(-3 87 14)">HANDCRAFTED IN FERNHOLLOW</text>
      </svg>
    </div>
  </section>

  <section class="box-panel box-panel--front">
    <div class="panel-pattern" role="img" aria-label="Abstract grey and cream brush-stroke pattern with dotted shapes"></div>
    <div class="label">
      <div class="label-frame"></div>
      <h1 class="product-name">Honey<br>Plum</h1>
      <div class="name-divider"></div>
      <p class="brand-name">Wattlebrook<br>Lather Co</p>
      <p class="web-address">WWW.LOREM IPSUM DOLOR.COM</p>
    </div>
  </section>

</main>
</body>
</html>
```